Modern Spot UV Business Card design

We are a relatively new real estate agency. We need a business card that reflects the professionalism and prestige of our company but is also modern and fresh, based around our logo.
We would love to utilise spot UV.
Happy to let the designers use their imagination and see what they come up with (we're not very creative, so have no ideas for you, sorry) :-)
We'd like one for each staff member, but I've just provided one staff members photo here to avoid confusion.

Target Market(s)

Families

Industry/Entity Type

Real Estate Agent

Contact Information for Business Card

Dale Verco - Director & Principal
Mobile: 0491 627 540
Email: dale.verco@vbrokers.example.au
Phone: (08) 8374 6150
Fax: (08) 8374 6198
www.vercobrokersproperty.example.au

Font styles to use
Other font styles liked:
• Kabel Dm BT

Requirements
Must have
• Contact details, logo, photo, spot UV
Nice to have
• Modern interesting features that will make people comment. Nothing too feminine nor too masculine.
Should not have
• No houses! Nothing typical of a real estate agent.

```html
<!DOCTYPE html>
<html lang="en">
<head>
<meta charset="utf-8">
<title>Verco Brokers Property – Business Card</title>
<link href="https://fonts.googleapis.com/css2?family=Arimo:wght@400;700&family=Mulish:wght@700;800&display=swap" rel="stylesheet">
<style>
  :root {
    --backdrop: #e9e7e4;
    --card: #1b1c1e;
    --card-edge: #111214;
    --brand-blue: #2a86c5;
    --accent-orange: #c27a34;
    --text-light: #f2f2f2;
    --text-muted: #8c8f94;
    --photo-top: #3a3d42;
    --photo-bottom: #5b5f66;
  }
  * { box-sizing: border-box; margin: 0; padding: 0; }
  html, body {
    width: 1200px; height: 864px; overflow: hidden;
    background: var(--backdrop);
    font-family: "Arimo", Arial, sans-serif;
  }
  .sheet {
    width: 1200px; height: 864px;
    display: flex; flex-direction: column;
    align-items: center; justify-content: center; gap: 30px;
  }
  .card {
    position: relative;
    width: 640px; height: 391px;
    background: var(--card);
    border: 1px solid var(--card-edge);
    border-radius: 3px;
    box-shadow: 0 6px 18px rgba(0,0,0,.25);
    overflow: hidden;
  }

  /* Back */
  .card-back { display: flex; flex-direction: column; align-items: center; justify-content: center; gap: 34px; }
  .monogram-name {
    font-family: "Mulish", sans-serif; font-weight: 800;
    font-size: 54px; color: var(--brand-blue); letter-spacing: .5px;
  }
  .back-web { font-size: 15px; color: var(--text-muted); letter-spacing: 1.2px; }

  /* Front */
  .brand { position: absolute; left: 40px; top: 46px; }
  .brand-name {
    font-family: "Mulish", sans-serif; font-weight: 800;
    font-size: 38px; color: var(--text-light); line-height: 1;
    display: flex; align-items: center; gap: 10px;
  }
  .brand-dot { width: 14px; height: 14px; border-radius: 50%; background: var(--accent-orange); }
  .brand-sub { display: flex; align-items: center; gap: 10px; margin-top: 6px; }
  .brand-division { font-size: 22px; color: #55585d; }
  .tagline {
    font-size: 11px; line-height: 1.15; color: #6f7277;
    border-left: 1px solid #55585d; padding-left: 8px;
  }
  .contact-list { position: absolute; left: 40px; top: 170px; list-style: none; }
  .contact-list li {
    display: flex; align-items: center; gap: 10px;
    font-size: 14px; color: var(--text-light); height: 24px;
  }
  .contact-list svg { width: 14px; height: 14px; fill: var(--brand-blue); flex: none; }
  .person { position: absolute; right: 36px; top: 108px; text-align: right; }
  .person-name { font-size: 19px; font-weight: 700; color: var(--brand-blue); }
  .person-role { font-size: 15px; color: var(--text-light); margin-top: 3px; }
  .portrait {
    position: absolute; right: 22px; bottom: 0;
    width: 250px; height: 190px;
    background: linear-gradient(180deg, var(--photo-top), var(--photo-bottom));
    border-radius: 120px 120px 0 0;
  }
</style>
</head>
<body>
<main class="sheet">

  <section class="card card-back" aria-label="Business card back">
    <div class="monogram-name">Verco Brokers</div>
    <div class="back-web">www.vercobrokersproperty.example.au</div>
  </section>

  <section class="card card-front" aria-label="Business card front">
    <div class="brand">
      <div class="brand-name"><span class="brand-dot"></span>Verco Brokers</div>
      <div class="brand-sub">
        <span class="brand-division">Property</span>
        <span class="tagline">Helping you make<br>your next move</span>
      </div>
    </div>

    <ul class="contact-list">
      <li><svg viewBox="0 0 16 16"><path d="M3 1l3 3-2 2c1 2 3 4 5 5l2-2 3 3-2 3C6 14 2 10 1 3z"/></svg>(08) 8374 6150</li>
      <li><svg viewBox="0 0 16 16"><path d="M4 0h8v16H4zM6 2v10h4V2z"/></svg>(08) 8374 6198</li>
      <li><svg viewBox="0 0 16 16"><path d="M3 1h10v4H3zM1 6h14v7H1zM4 10h8v5H4z"/></svg>0491 627 540</li>
      <li><svg viewBox="0 0 16 16"><path d="M0 3h16v10H0zM1 4l7 5 7-5v-.5H1z"/></svg>dale.verco@vbrokers.example.au</li>
      <li><svg viewBox="0 0 16 16"><circle cx="8" cy="8" r="7"/></svg>vercobrokersproperty.example.au</li>
    </ul>

    <div class="person">
      <div class="person-name">Dale Verco</div>
      <div class="person-role">Director &amp; Principal</div>
    </div>

    <div class="portrait" role="img" aria-label="Portrait photo of the agent in a grey suit"></div>
  </section>

</main>
</body>
</html>
```